Update Old OR create new Website

Current Website is looking a bit old, I did this one a few years back.

Would like a fresh new look, current website sitepress theme is " the Vanta theme" from plumcrate and I just purchased this theme - "bravlo" also from plumcrate, I quite like the look of - http://bravlo.quorvex-skins.com/tech-business/ and if we could get somthing simlar would be great.

current website is at http://www.hle.com.au, have been playing around with the slider that i like.

I have said 5 pages to be designed but really it is just a 5 page website where most pages will look the same.

Any questions please let me know

Target Market(s)

Business

Coding

Coded - Design and coding required

Number of Pages Required

5+ page

Font styles to use
Sans Serif

Colors
33a6d7
0292cd
ffffff
0255a3

Requirements
Must have
• Device compatibility - pc, tablet, phone
Nice to have
• video
Should not have
• vunerabilities. Must also use images that will expire or disappear, ie must be uploaded to site not links to elsewhere.

```html
<!DOCTYPE html>
<html lang="en">
<head>
<meta charset="utf-8">
<title>HLE Technologies</title>
<link href="https://fonts.googleapis.com/css2?family=Roboto:wght@400;500;700&display=swap" rel="stylesheet">
<style>
:root{
  --blue:#0fa9d6;
  --blue-deep:#0292cd;
  --navy:#1b2230;
  --navy-2:#141a26;
  --ink:#1f2430;
  --grey:#666d78;
  --line:#e3e6ea;
  --soft:#f5f5f6;
  --white:#ffffff;
}
*{box-sizing:border-box;margin:0;padding:0}
html,body{width:1200px;height:2812px;overflow:hidden}
body{font-family:"Roboto",Arial,sans-serif;color:var(--ink);background:var(--white);position:relative}
a{color:inherit;text-decoration:none}

/* top bar */
.topbar{position:absolute;top:0;left:0;width:1200px;height:38px;background:var(--navy);color:#cfd4dc;font-size:12px}
.topbar .info{position:absolute;top:0;height:38px;display:flex;align-items:center;gap:6px}
.topbar .addr{left:544px}
.topbar .mail{left:778px}
.topbar .call{position:absolute;left:904px;top:0;width:206px;height:38px;background:var(--blue);color:var(--white);display:flex;align-items:center;justify-content:center;gap:8px;font-size:13px;font-weight:500}

/* header */
.header{position:absolute;top:38px;left:0;width:1200px;height:97px;background:var(--white);border-bottom:1px solid var(--line)}
.brand{position:absolute;left:88px;top:31px;display:flex;align-items:center;gap:10px;height:34px}
.brand .mark{width:30px;height:30px;background:var(--blue)}
.brand .name{font-size:21px;font-weight:500;color:var(--ink);line-height:1}
.nav{position:absolute;left:469px;top:37px;display:flex;align-items:center;font-size:13px;font-weight:500}
.nav a{height:28px;display:flex;align-items:center;padding:0 16px}
.nav a.active{background:var(--blue);color:var(--white);width:69px;justify-content:center;margin-right:8px}
.nav .search{margin-left:8px}

/* hero */
.hero{position:absolute;top:135px;left:0;width:1200px;height:553px;background:linear-gradient(180deg,#555d7a 0%,#4a5270 55%,#3f4763 100%);text-align:center;color:var(--white)}
.hero .scene{position:absolute;inset:0;background:radial-gradient(ellipse at 70% 30%,rgba(140,150,185,.45),transparent 60%)}
.hero h1{position:absolute;top:223px;left:0;width:100%;font-size:49px;font-weight:500;letter-spacing:-.5px}
.hero p{position:absolute;top:288px;left:300px;width:600px;font-size:14px;line-height:23px;color:#eef0f5}
.hero .btn{position:absolute;left:538px;top:349px;width:126px;height:37px;background:var(--blue);font-size:12px;font-weight:500;display:flex;align-items:center;justify-content:center}

/* services */
.services{position:absolute;top:688px;left:0;width:1200px;height:452px}
.card{position:absolute;top:85px;width:244px;height:290px;border:1px solid var(--line);text-align:center;padding:0 18px}
.card svg{margin-top:62px}
.card h3{font-size:15px;font-weight:500;margin-top:10px}
.card p{font-size:11.5px;color:var(--grey);line-height:20px;margin-top:10px}

/* about */
.about{position:absolute;top:1140px;left:0;width:1200px;height:411px;background:var(--soft)}
.about .photo{position:absolute;left:160px;top:26px;width:356px;height:385px;background:linear-gradient(180deg,#e9ecef,#cfd5dc)}
.about h2{position:absolute;left:581px;top:98px;width:475px;font-size:22px;font-weight:500;line-height:31px}
.about p{position:absolute;left:581px;top:204px;width:480px;font-size:12px;line-height:22px;color:var(--grey)}
.about .btn{position:absolute;left:585px;top:296px;width:115px;height:38px;border:1px solid #c9cdd2;background:var(--white);font-size:11px;font-weight:500;display:flex;align-items:center;justify-content:center}

/* testimonials */
.reviews{position:absolute;top:1551px;left:0;width:1200px;height:560px;background:linear-gradient(180deg,#12aed6,#0b97c4);color:var(--white)}
.reviews h2{position:absolute;top:100px;width:100%;text-align:center;font-size:26px;font-weight:500}
.quote{position:absolute;top:180px;width:326px;height:183px;background:rgba(255,255,255,.14);padding:26px 30px}
.quote h4{font-size:15px;font-weight:500}
.quote p{font-size:12px;line-height:22px;margin-top:16px;color:#eef8fc}
.quote::after{content:"";position:absolute;left:56px;bottom:-14px;border:7px solid transparent;border-top-color:rgba(255,255,255,.14);border-left-color:rgba(255,255,255,.14)}
.author{position:absolute;top:400px;display:flex;align-items:center;gap:14px}
.author .avatar{width:60px;height:60px;border-radius:50%;background:#2f3b48;border:2px solid rgba(255,255,255,.5)}
.author b{display:block;font-size:15px;font-weight:500}
.author span{font-size:11.5px;color:#e2f3fa}
.arrow{position:absolute;top:236px;width:32px;height:69px;background:#0a6f94;display:flex;align-items:center;justify-content:center}
.arrow.left{left:0}.arrow.right{right:0}

/* news */
.news{position:absolute;top:2111px;left:0;width:1200px;height:351px;text-align:center}
.news h2{margin-top:114px;font-size:25px;font-weight:500}
.news p{margin-top:8px;font-size:12px;color:var(--grey)}
.partners{position:absolute;top:209px;left:155px;width:890px;display:flex;justify-content:space-between;align-items:center}
.partners span{font-size:36px;font-weight:500;color:#a4a8ae;width:180px}

/* footer */
.footer{position:absolute;top:2462px;left:0;width:1200px;height:350px;background:var(--navy-2);color:#c4c9d1}
.col{position:absolute;top:70px}
.col h5{font-size:13px;font-weight:500;color:var(--white);margin-bottom:14px}
.col li{list-style:none;font-size:12px;line-height:25px}
.socials{display:flex;gap:13px;margin-top:4px}
.socials i{width:30px;height:30px;border-radius:50%;background:#262e3d;display:block}
.footer .rule{position:absolute;top:302px;left:88px;width:1024px;height:1px;background:#2a3243}
.footer .copy{position:absolute;top:320px;width:100%;text-align:center;font-size:11px;color:var(--white);font-weight:500}
.totop{position:absolute;left:1114px;top:287px;width:30px;height:30px;border-radius:50%;background:var(--blue);display:flex;align-items:center;justify-content:center}
</style>
</head>
<body>

<div class="topbar">
  <div class="info addr"><svg width="10" height="12" viewBox="0 0 10 12"><path d="M5 0a4 4 0 0 0-4 4c0 3 4 8 4 8s4-5 4-8a4 4 0 0 0-4-4zm0 5.5A1.5 1.5 0 1 1 5 2.5a1.5 1.5 0 0 1 0 3z" fill="#cfd4dc"/></svg>14b 2270 Harlow Rd, Upper Mt Ferris</div>
  <div class="info mail"><svg width="11" height="8" viewBox="0 0 11 8"><rect width="11" height="8" fill="#cfd4dc"/><path d="M0 0l5.5 4L11 0" stroke="#1b2230" fill="none"/></svg>info@hle.com.au</div>
  <div class="call"><svg width="13" height="13" viewBox="0 0 24 24"><path d="M6.6 10.8a15 15 0 0 0 6.6 6.6l2.2-2.2c.3-.3.7-.4 1-.2 1.1.4 2.3.6 3.6.6.6 0 1 .4 1 1V20c0 .6-.4 1-1 1A17 17 0 0 1 3 4c0-.6.4-1 1-1h3.5c.6 0 1 .4 1 1 0 1.3.2 2.5.6 3.6.1.3 0 .7-.2 1z" fill="#fff"/></svg>Call now ! 1300 482 519</div>
</div>

<header class="header">
  <a class="brand" href="#"><span class="mark"></span><span class="name">HLE Technologies</span></a>
  <nav class="nav">
    <a class="active" href="#">Home</a>
    <a href="#">Servers</a>
    <a href="#">Networks</a>
    <a href="#">Managed IT</a>
    <a href="#">Web</a>
    <a href="#">App's</a>
    <a href="#">Internet</a>
    <a href="#">Contact</a>
    <svg class="search" width="13" height="13" viewBox="0 0 13 13"><circle cx="5.5" cy="5.5" r="4.2" stroke="#1f2430" stroke-width="1.8" fill="none"/><path d="M8.6 8.6L12 12" stroke="#1f2430" stroke-width="1.8"/></svg>
  </nav>
</header>

<section class="hero">
  <div class="scene" role="img" aria-label="Blurred screen of code with a network of connected dots"></div>
  <h1>THE POWER OF TECHNOLOGY</h1>
  <p>Lorem ipsum dolor sit amet, consectetuer adipiscing elit. Aenean commodo ligula eget dolor<br>penatibus et magnis dis parturient montes nascetur .</p>
  <a class="btn" href="#">CHECK IT OUT</a>
</section>

<section class="services">
  <div class="card" style="left:88px">
    <svg width="58" height="58" viewBox="0 0 58 58" fill="none" stroke="#0fa9d6" stroke-width="2"><rect x="6" y="4" width="46" height="14" rx="2"/><rect x="6" y="22" width="46" height="14" rx="2"/><rect x="6" y="40" width="46" height="14" rx="2"/><circle cx="13" cy="11" r="2"/><circle cx="13" cy="29" r="2"/><circle cx="13" cy="47" r="2"/><path d="M32 11h14M32 29h14M32 47h14"/></svg>
    <h3>Servers</h3>
    <p>HLE Technologies provides design, support and maintenance for quality I.T Systems</p>
  </div>
  <div class="card" style="left:347px">
    <svg width="58" height="58" viewBox="0 0 58 58" fill="none" stroke="#0fa9d6" stroke-width="2"><circle cx="29" cy="29" r="6"/><circle cx="10" cy="10" r="5"/><circle cx="48" cy="10" r="5"/><circle cx="10" cy="48" r="5"/><circle cx="48" cy="48" r="5"/><circle cx="29" cy="6" r="4"/><path d="M14 14l10 10M44 14L34 24M14 44l10-10M44 44L34 34M29 10v13"/></svg>
    <h3>Networks</h3>
    <p>With over a decade of experience, HLE Technologies understands the challenges faced .</p>
  </div>
  <div class="card" style="left:608px">
    <svg width="58" height="58" viewBox="0 0 58 58" fill="none" stroke="#0fa9d6" stroke-width="2"><circle cx="29" cy="29" r="20"/><circle cx="29" cy="10" r="5" fill="#fff"/><circle cx="10" cy="33" r="5" fill="#fff"/><circle cx="48" cy="33" r="5" fill="#fff"/><circle cx="29" cy="29" r="4"/><path d="M21 52c2-6 14-6 16 0"/></svg>
    <h3>Managed IT</h3>
    <p>Clients choose HLE Technologies because HLE's core focus is on anticipating .</p>
  </div>
  <div class="card" style="left:867px">
    <svg width="58" height="58" viewBox="0 0 58 58" fill="none" stroke="#0fa9d6" stroke-width="2"><circle cx="29" cy="29" r="24"/><ellipse cx="29" cy="29" rx="11" ry="24"/><path d="M5 29h48M9 17h40M9 41h40M29 5v48"/></svg>
    <h3>Internet</h3>
    <p>Having access to the leading providers of Internet in Australia we can determine not only who.</p>
  </div>
</section>

<section class="about">
  <div class="photo" role="img" aria-label="Smiling support technician with a headset holding a laptop"></div>
  <h2>What would it take for your information systems to actually improve the performance of your organisation?</h2>
  <p>Through HLE Technologies, companies outsource all the expertise they need to secure their systems and optimise the output of their people and IT resources – without the expense of maintaining large internal IT departments.</p>
  <a class="btn" href="#">READ MORE</a>
</section>

<section class="reviews">
  <h2>See what our clients say</h2>
  <a class="arrow left" href="#"><svg width="8" height="12" viewBox="0 0 8 12"><path d="M6 1L1 6l5 5" stroke="#fff" stroke-width="2" fill="none"/></svg></a>
  <a class="arrow right" href="#"><svg width="8" height="12" viewBox="0 0 8 12"><path d="M2 1l5 5-5 5" stroke="#fff" stroke-width="2" fill="none"/></svg></a>

  <div class="quote" style="left:88px"><h4>Super Support!</h4><p>"Etiam aenean imperdietultricies nisi vel augue curabitur ullamcorper ultricies lorem.<br>Aenean imperdietultricies nisi vel augue lorem curabitur ullamcorper ultricies ipsum."</p></div>
  <div class="quote" style="left:437px"><h4>Super Support!</h4><p>"Etiam aenean imperdietultricies nisi vel augue curabitur ullamcorper ultricies lorem.<br>Aenean imperdietultricies nisi vel augue lorem curabitur ullamcorper ultricies ipsum."</p></div>
  <div class="quote" style="left:786px"><h4>Super Support!</h4><p>"Etiam aenean imperdietultricies nisi vel augue curabitur ullamcorper ultricies lorem.<br>Aenean imperdietultricies nisi vel augue lorem curabitur ullamcorper ultricies ipsum."</p></div>

  <div class="author" style="left:88px"><div class="avatar" role="img" aria-label="Portrait of the client"></div><div><b>Owen Hartley</b><span>Designer at tech company</span></div></div>
  <div class="author" style="left:437px"><div class="avatar" role="img" aria-label="Portrait of the client"></div><div><b>Marla Quinn</b><span>HR at ABC company</span></div></div>
  <div class="author" style="left:786px"><div class="avatar" role="img" aria-label="Portrait of the client"></div><div><b>Reid Collins</b><span>Manager at tech company</span></div></div>
</section>

<section class="news">
  <h2>Stay Up To Date With The Latest News</h2>
  <p>Lorem ipsum dolor sit amet, consectetuer adipiscing elit</p>
  <div class="partners"><span>Lumora</span><span>Brightpath</span><span>Tessaly</span><span>Norvend</span></div>
</section>

<footer class="footer">
  <div class="col" style="left:88px"><h5>SERVICES</h5><ul><li>Servers</li><li>Networks</li><li>Manage IT</li><li>Web</li><li>Apps</li><li>Internet</li></ul></div>
  <div class="col" style="left:386px"><h5>INFORMATION</h5><ul><li>About us</li><li>Customers</li><li>Reviews</li><li>Clients</li><li>Services</li><li>Announcements</li></ul></div>
  <div class="col" style="left:649px"><h5>LEGAL</h5><ul><li>Manufacturers</li><li>Privacy Policy</li><li>Terms &amp; Conditions</li></ul></div>
  <div class="col" style="left:894px"><h5>FOLLOW US</h5><div class="socials"><i aria-label="Social profile"></i><i aria-label="Social profile"></i><i aria-label="Social profile"></i><i aria-label="Social profile"></i></div></div>
  <div class="rule"></div>
  <a class="totop" href="#"><svg width="12" height="8" viewBox="0 0 12 8"><path d="M1 7l5-5 5 5" stroke="#fff" stroke-width="2" fill="none"/></svg></a>
  <div class="copy">HLE TECHNOLOGIES COPYRIGHT 2017</div>
</footer>

</body>
</html>
```